Exciting new aperitif brand needs a great label

Vel-Orin is a wonderful rich new premium-priced bitter aperitif, with a deep red colour, from a 100+ year old distillery (1890) near Turin in the Piedmont region of Italy. Inspired by Torvesi, it is perfectly formulated to elevate the classic Baldetti cocktail (and variations on it). It also goes perfectly in a Spritz or a long mixed drink with soda or tonic. The name Vel-Orin is derived from the French for 'peak' and the Italian word for 'love'.

The label, which should take inspiration from Torvesi, but be distinctively different, can incoporate any number of premium label embellishments (foil, embossing, textures etc) and should be no greater than 11cm (height) x 9cm (width) with any core imagery restricted to a width of c.7cm.

The attached mood board should act as inspiration and colour should largely be restricted to reds, blues, whites and perhaps orange. For completeness, the label should note that the ABV is 25% and the bottle size 70cl.

Target Market(s)

21-45yr olds - equal split female/male

Colors
0054AA
0677BA
7BADD7
CADEEF
E8F1F8
0094D4
00A9DD
6FCCEA
C7EBF8
E9F6FB
EE7325
F08F49
F5BC92
FAE3D3
FDF4ED
EB3D1F
EC4F4E
F09395
F8D3D4
FCEDEE

Requirements
Must have
• Great lettering design on the name Vel-Orin

```html
<!DOCTYPE html>
<html lang="en">
<head>
<meta charset="utf-8">
<title>Vel-Orin Aperitivo Label – Print Separations</title>
<link rel="stylesheet" href="https://fonts.googleapis.com/css2?family=Arimo:wght@400;700&family=Cinzel:wght@700&family=Libre+Bodoni:wght@400;700&family=Oswald:wght@400;600&family=Pinyon+Script&display=swap">
<style>
  :root{
    --canvas:#0a0a0c;
    --paper:#d9ebf8;
    --paper-light:#e8f3fb;
    --navy:#0b3a78;
    --navy-stripe:#1f4f8f;
    --red:#d8261c;
    --gold:#f0b21a;
    --gold-deep:#c98a0c;
    --grey:#a3a3a3;
    --grey-deep:#7e7e7e;
    --varnish:#e0147a;
    --varnish-dim:#6a0e40;
    --white:#ffffff;
    --cyan:#0a9be0;
    --magenta:#e0148c;
    --yellow:#f4e300;
    --key:#2a2a2a;
  }
  *{margin:0;padding:0;box-sizing:border-box}
  html,body{width:1200px;height:996px;overflow:hidden;background:var(--canvas)}
  body{position:relative;font-family:"Arimo",Arial,sans-serif;color:var(--white)}
  .shared-defs{position:absolute;width:0;height:0;overflow:hidden}
  .panel-title{position:absolute;transform:translateX(-50%);white-space:nowrap;line-height:1}
  .panel-title--preview{left:602px;top:14px;font-size:30px}
  .panel-title--print{left:210px;top:494px;font-size:27px;font-weight:700}
  .panel-title--foil{left:588px;top:494px;font-size:28px}
  .panel-title--varnish{left:964px;top:490px;font-size:22px}
  .ink-c{color:var(--cyan)} .ink-m{color:var(--magenta)} .ink-y{color:var(--yellow)} .ink-k{color:var(--key)}
  .label{position:absolute;width:330px;height:403px}
  .label--preview{left:437px;top:58px}
  .label--print{left:50px;top:537px}
  .label--foil{left:423px;top:537px}
  .label--varnish{left:802px;top:537px}
  .wordmark{font-family:"Cinzel",serif;font-weight:700}
  .bodoni{font-family:"Libre Bodoni",serif}
  .condensed{font-family:"Oswald",sans-serif}
  .script{font-family:"Pinyon Script",cursive}
</style>
</head>
<body>

<svg class="shared-defs" aria-hidden="true">
  <defs>
    <radialGradient id="paper-tone" cx="50%" cy="50%" r="70%">
      <stop offset="0" stop-color="#e6f2fb"/>
      <stop offset="1" stop-color="#cfe3f3"/>
    </radialGradient>
    <radialGradient id="gold-ornament" cx="50%" cy="50%" r="50%">
      <stop offset="0" stop-color="#f4bd2a" stop-opacity=".95"/>
      <stop offset=".6" stop-color="#f0b21a" stop-opacity=".6"/>
      <stop offset="1" stop-color="#f0b21a" stop-opacity="0"/>
    </radialGradient>
    <radialGradient id="grey-ornament" cx="50%" cy="50%" r="50%">
      <stop offset="0" stop-color="#a8a8a8" stop-opacity=".9"/>
      <stop offset=".6" stop-color="#a3a3a3" stop-opacity=".55"/>
      <stop offset="1" stop-color="#a3a3a3" stop-opacity="0"/>
    </radialGradient>
    <radialGradient id="red-accent" cx="50%" cy="50%" r="50%">
      <stop offset="0" stop-color="#d8261c" stop-opacity=".9"/>
      <stop offset="1" stop-color="#d8261c" stop-opacity="0"/>
    </radialGradient>
    <radialGradient id="varnish-pattern" cx="50%" cy="50%" r="65%">
      <stop offset="0" stop-color="#a3155f"/>
      <stop offset="1" stop-color="#5a0c36"/>
    </radialGradient>
    <linearGradient id="band-shade" x1="0" y1="0" x2="1" y2="0">
      <stop offset="0" stop-color="#072c60"/>
      <stop offset=".5" stop-color="#0d4188"/>
      <stop offset="1" stop-color="#072c60"/>
    </linearGradient>
  </defs>
</svg>

<div class="panel-title panel-title--preview">Preview</div>

<!-- Full-colour label -->
<svg class="label label--preview" viewBox="0 0 577 705" aria-label="Vel-Orin aperitivo label, finished look">
  <rect width="577" height="705" fill="url(#paper-tone)" role="img" aria-label="Pale blue embossed interlaced knotwork background"/>
  <line x1="12" y1="16" x2="565" y2="16" stroke="var(--gold)" stroke-width="8" stroke-dasharray="7 4"/>
  <line x1="12" y1="690" x2="198" y2="690" stroke="var(--gold)" stroke-width="8" stroke-dasharray="7 4"/>
  <line x1="378" y1="690" x2="565" y2="690" stroke="var(--gold)" stroke-width="8" stroke-dasharray="7 4"/>
  <rect x="245" y="44" width="86" height="55" fill="var(--red)" stroke="var(--navy)" stroke-width="3"/>
  <rect x="281" y="56" width="14" height="38" fill="var(--white)"/>
  <rect x="258" y="68" width="60" height="13" fill="var(--white)"/>
  <g role="img" aria-label="Gold baroque scroll ornament with red flames">
    <ellipse cx="288" cy="140" rx="175" ry="44" fill="url(#gold-ornament)"/>
    <ellipse cx="150" cy="124" rx="26" ry="24" fill="url(#red-accent)"/>
    <ellipse cx="426" cy="124" rx="26" ry="24" fill="url(#red-accent)"/>
  </g>
  <text x="288" y="130" text-anchor="middle" class="script" font-size="28" fill="var(--gold-deep)">Piedmont</text>
  <path d="M0 212H150C190 212 200 188 288 188S386 212 427 212H577V405H427C386 405 376 427 288 427S190 405 150 405H0Z" fill="url(#band-shade)"/>
  <g stroke="var(--navy-stripe)" stroke-width="2">
    <line x1="0" y1="230" x2="60" y2="230"/><line x1="0" y1="240" x2="60" y2="240"/><line x1="0" y1="250" x2="60" y2="250"/>
    <line x1="0" y1="360" x2="60" y2="360"/><line x1="0" y1="370" x2="60" y2="370"/><line x1="0" y1="380" x2="60" y2="380"/>
    <line x1="517" y1="230" x2="577" y2="230"/><line x1="517" y1="240" x2="577" y2="240"/><line x1="517" y1="250" x2="577" y2="250"/>
    <line x1="517" y1="360" x2="577" y2="360"/><line x1="517" y1="370" x2="577" y2="370"/><line x1="517" y1="380" x2="577" y2="380"/>
  </g>
  <path d="M0 214H150C190 214 200 190 288 190S386 214 427 214H577" fill="none" stroke="var(--gold)" stroke-width="5"/>
  <path d="M0 403H150C190 403 200 425 288 425S386 403 427 403H577" fill="none" stroke="var(--gold)" stroke-width="5"/>
  <ellipse cx="288" cy="226" rx="52" ry="18" fill="url(#gold-ornament)" role="img" aria-label="Small gold fan ornament"/>
  <text x="288" y="348" text-anchor="middle" class="wordmark" font-size="88" textLength="469" lengthAdjust="spacingAndGlyphs" fill="var(--white)">VEL-ORIN</text>
  <path id="arc-preview" d="M212 390Q288 418 364 390" fill="none"/>
  <text class="bodoni" font-size="18" fill="var(--white)" letter-spacing="6"><textPath href="#arc-preview" startOffset="50%" text-anchor="middle">Since 1890</textPath></text>
  <text x="288" y="536" text-anchor="middle" class="condensed" font-size="64" font-weight="600" textLength="266" lengthAdjust="spacingAndGlyphs" fill="var(--red)">APERETIVO</text>
  <text x="288" y="573" text-anchor="middle" class="condensed" font-size="22" textLength="172" lengthAdjust="spacingAndGlyphs" fill="var(--red)">premium-priced bitter</text>
  <text x="78" y="536" text-anchor="middle" class="bodoni" font-size="20" fill="var(--navy)">25% vol.</text>
  <text x="508" y="536" text-anchor="middle" class="bodoni" font-size="20" fill="var(--navy)">700 ml.</text>
  <g role="img" aria-label="Gold floral corner ornaments with red blossoms">
    <ellipse cx="98" cy="610" rx="78" ry="66" fill="url(#gold-ornament)"/>
    <ellipse cx="55" cy="568" rx="20" ry="20" fill="url(#red-accent)"/>
    <ellipse cx="142" cy="655" rx="20" ry="20" fill="url(#red-accent)"/>
    <ellipse cx="478" cy="610" rx="78" ry="66" fill="url(#gold-ornament)"/>
    <ellipse cx="521" cy="568" rx="20" ry="20" fill="url(#red-accent)"/>
    <ellipse cx="434" cy="655" rx="20" ry="20" fill="url(#red-accent)"/>
  </g>
  <rect x="205" y="642" width="166" height="50" fill="var(--red)" stroke="var(--gold)" stroke-width="3"/>
  <text x="288" y="661" text-anchor="middle" class="bodoni" font-size="12" letter-spacing="2" fill="var(--white)">PRODUCED BY</text>
  <text x="288" y="684" text-anchor="middle" class="bodoni" font-size="20" letter-spacing="4" fill="var(--white)">ITALY</text>
</svg>

<div class="panel-title panel-title--print">Print&nbsp; <span class="ink-c">C</span><span class="ink-m">M</span><span class="ink-y">Y</span><span class="ink-k">K</span></div>

<!-- CMYK plate -->
<svg class="label label--print" viewBox="0 0 577 705" aria-label="Vel-Orin label, CMYK print layer">
  <rect width="577" height="705" fill="url(#paper-tone)" role="img" aria-label="Pale blue embossed interlaced knotwork background"/>
  <line x1="12" y1="16" x2="565" y2="16" stroke="var(--grey)" stroke-width="8" stroke-dasharray="7 4"/>
  <line x1="12" y1="690" x2="198" y2="690" stroke="var(--grey)" stroke-width="8" stroke-dasharray="7 4"/>
  <line x1="378" y1="690" x2="565" y2="690" stroke="var(--grey)" stroke-width="8" stroke-dasharray="7 4"/>
  <rect x="245" y="44" width="86" height="55" fill="var(--red)" stroke="var(--navy)" stroke-width="3"/>
  <rect x="281" y="56" width="14" height="38" fill="var(--white)"/>
  <rect x="258" y="68" width="60" height="13" fill="var(--white)"/>
  <g role="img" aria-label="Grey scroll ornament with red flames">
    <ellipse cx="288" cy="140" rx="175" ry="44" fill="url(#grey-ornament)"/>
    <ellipse cx="150" cy="124" rx="26" ry="24" fill="url(#red-accent)"/>
    <ellipse cx="426" cy="124" rx="26" ry="24" fill="url(#red-accent)"/>
  </g>
  <text x="288" y="130" text-anchor="middle" class="script" font-size="28" fill="var(--grey-deep)">Piedmont</text>
  <path d="M0 212H150C190 212 200 188 288 188S386 212 427 212H577V405H427C386 405 376 427 288 427S190 405 150 405H0Z" fill="url(#band-shade)"/>
  <g stroke="var(--navy-stripe)" stroke-width="2">
    <line x1="0" y1="230" x2="60" y2="230"/><line x1="0" y1="240" x2="60" y2="240"/><line x1="0" y1="250" x2="60" y2="250"/>
    <line x1="0" y1="360" x2="60" y2="360"/><line x1="0" y1="370" x2="60" y2="370"/><line x1="0" y1="380" x2="60" y2="380"/>
    <line x1="517" y1="230" x2="577" y2="230"/><line x1="517" y1="240" x2="577" y2="240"/><line x1="517" y1="250" x2="577" y2="250"/>
    <line x1="517" y1="360" x2="577" y2="360"/><line x1="517" y1="370" x2="577" y2="370"/><line x1="517" y1="380" x2="577" y2="380"/>
  </g>
  <text x="288" y="348" text-anchor="middle" class="wordmark" font-size="88" textLength="469" lengthAdjust="spacingAndGlyphs" fill="var(--white)">VEL-ORIN</text>
  <path id="arc-print" d="M212 390Q288 418 364 390" fill="none"/>
  <text class="bodoni" font-size="18" fill="var(--white)" letter-spacing="6"><textPath href="#arc-print" startOffset="50%" text-anchor="middle">Since 1890</textPath></text>
  <text x="288" y="536" text-anchor="middle" class="condensed" font-size="64" font-weight="600" textLength="266" lengthAdjust="spacingAndGlyphs" fill="var(--red)">APERETIVO</text>
  <text x="288" y="573" text-anchor="middle" class="condensed" font-size="22" textLength="172" lengthAdjust="spacingAndGlyphs" fill="var(--red)">premium-priced bitter</text>
  <text x="78" y="536" text-anchor="middle" class="bodoni" font-size="20" fill="var(--navy)">25% vol.</text>
  <text x="508" y="536" text-anchor="middle" class="bodoni" font-size="20" fill="var(--navy)">700 ml.</text>
  <g role="img" aria-label="Grey floral corner ornaments with red blossoms">
    <ellipse cx="98" cy="610" rx="78" ry="66" fill="url(#grey-ornament)"/>
    <ellipse cx="55" cy="568" rx="20" ry="20" fill="url(#red-accent)"/>
    <ellipse cx="142" cy="655" rx="20" ry="20" fill="url(#red-accent)"/>
    <ellipse cx="478" cy="610" rx="78" ry="66" fill="url(#grey-ornament)"/>
    <ellipse cx="521" cy="568" rx="20" ry="20" fill="url(#red-accent)"/>
    <ellipse cx="434" cy="655" rx="20" ry="20" fill="url(#red-accent)"/>
  </g>
  <rect x="205" y="642" width="166" height="50" fill="var(--red)"/>
  <text x="288" y="661" text-anchor="middle" class="bodoni" font-size="12" letter-spacing="2" fill="var(--white)">PRODUCED BY</text>
  <text x="288" y="684" text-anchor="middle" class="bodoni" font-size="20" letter-spacing="4" fill="var(--white)">ITALY</text>
</svg>

<div class="panel-title panel-title--foil">Hot foil shtamping</div>

<!-- Gold foil plate -->
<svg class="label label--foil" viewBox="0 0 577 705" aria-label="Vel-Orin label, hot foil layer">
  <line x1="12" y1="36" x2="565" y2="36" stroke="var(--gold)" stroke-width="8" stroke-dasharray="7 4"/>
  <line x1="12" y1="690" x2="198" y2="690" stroke="var(--gold)" stroke-width="8" stroke-dasharray="7 4"/>
  <line x1="378" y1="690" x2="565" y2="690" stroke="var(--gold)" stroke-width="8" stroke-dasharray="7 4"/>
  <ellipse cx="288" cy="145" rx="175" ry="44" fill="url(#gold-ornament)" role="img" aria-label="Gold baroque scroll ornament"/>
  <text x="288" y="135" text-anchor="middle" class="script" font-size="28" fill="var(--gold-deep)">Piedmont</text>
  <path d="M0 214H150C190 214 200 190 288 190S386 214 427 214H577" fill="none" stroke="var(--gold)" stroke-width="5"/>
  <path d="M0 403H150C190 403 200 425 288 425S386 403 427 403H577" fill="none" stroke="var(--gold)" stroke-width="5"/>
  <ellipse cx="288" cy="228" rx="52" ry="18" fill="url(#gold-ornament)" role="img" aria-label="Small gold fan ornament"/>
  <text x="288" y="348" text-anchor="middle" class="wordmark" font-size="88" textLength="469" lengthAdjust="spacingAndGlyphs" fill="var(--gold)">VEL-ORIN</text>
  <path id="arc-foil" d="M212 390Q288 418 364 390" fill="none"/>
  <text class="bodoni" font-size="18" fill="var(--gold)" letter-spacing="6"><textPath href="#arc-foil" startOffset="50%" text-anchor="middle">Since 1890</textPath></text>
  <g role="img" aria-label="Gold floral corner ornaments">
    <ellipse cx="98" cy="610" rx="78" ry="66" fill="url(#gold-ornament)"/>
    <ellipse cx="478" cy="610" rx="78" ry="66" fill="url(#gold-ornament)"/>
  </g>
  <rect x="205" y="642" width="166" height="50" fill="none" stroke="var(--gold)" stroke-width="3"/>
</svg>

<div class="panel-title panel-title--varnish">Gloss Emboss Varnish</div>

<!-- Varnish plate -->
<svg class="label label--varnish" viewBox="0 0 577 705" aria-label="Vel-Orin label, gloss emboss varnish layer">
  <path d="M0 130C0 40 120 0 288 0S577 40 577 130V205H0Z" fill="url(#varnish-pattern)" role="img" aria-label="Interlaced knotwork emboss pattern"/>
  <rect x="245" y="44" width="86" height="55" fill="var(--varnish)"/>
  <g stroke="var(--varnish)" stroke-width="3">
    <line x1="0" y1="225" x2="577" y2="225"/><line x1="0" y1="240" x2="577" y2="240"/>
    <line x1="0" y1="255" x2="577" y2="255"/><line x1="0" y1="362" x2="577" y2="362"/>
    <line x1="0" y1="377" x2="577" y2="377"/><line x1="0" y1="392" x2="577" y2="392"/>
  </g>
  <rect x="40" y="262" width="497" height="96" fill="var(--canvas)"/>
  <text x="288" y="348" text-anchor="middle" class="wordmark" font-size="88" textLength="469" lengthAdjust="spacingAndGlyphs" fill="var(--varnish)">VEL-ORIN</text>
  <path id="arc-varnish" d="M212 400Q288 428 364 400" fill="none"/>
  <text class="bodoni" font-size="18" fill="var(--varnish)" letter-spacing="6"><textPath href="#arc-varnish" startOffset="50%" text-anchor="middle">Since 1890</textPath></text>
  <path d="M0 440H577V600C577 680 420 705 288 705S0 680 0 600Z" fill="url(#varnish-pattern)" role="img" aria-label="Interlaced knotwork emboss pattern with floral corners"/>
  <text x="288" y="560" text-anchor="middle" class="condensed" font-size="64" font-weight="600" textLength="266" lengthAdjust="spacingAndGlyphs" fill="var(--varnish)">APERETIVO</text>
  <text x="288" y="597" text-anchor="middle" class="condensed" font-size="22" textLength="172" lengthAdjust="spacingAndGlyphs" fill="var(--varnish)">premium-priced bitter</text>
  <text x="78" y="560" text-anchor="middle" class="bodoni" font-size="20" fill="var(--varnish)">25% vol.</text>
  <text x="508" y="560" text-anchor="middle" class="bodoni" font-size="20" fill="var(--varnish)">700 ml.</text>
  <rect x="210" y="648" width="156" height="46" fill="var(--varnish)"/>
</svg>

</body>
</html>
```